Business Card Design

We need a business card design for a Dry cleaners in Brisbane, Australia. We are trying to promote a fresh/clean image consistent with our website. www.quillpresswash.com.au

Looking for a professional neat card that's easy to read.

Target Market(s)

Customers looking for a professional, fresh and clean drycleaners.

Industry/Entity Type

Business

Contact Information for Business Card

See our existing business card. The Fax number (07) 3468 5203 to be removed.

Requirements
Must have
• All the details on current business card less the fax number.
Nice to have
• I like white text on coloured background. Blue works well as we are located near the water...

```html
<!DOCTYPE html>
<html lang="en">
<head>
<meta charset="utf-8">
<title>Quill Press Wash – Business Card Options</title>
<link rel="stylesheet" href="https://fonts.googleapis.com/css2?family=Arimo&family=PT+Sans:wght@400;700&family=Tinos:ital,wght@0,700;1,400;1,700&family=Dancing+Script:wght@700&display=swap">
<style>
  :root {
    --page: #ffffff;
    --label: #c9c9c9;
    --ink: #111111;
    --brand: #1f4f9e;
    --water-light: #b9d3ef;
    --water-mid: #6f9fd6;
    --water-deep: #4a7fc4;
    --band: #1b63b3;
    --band-line: #e8eef7;
    --card3: #1c67b4;
    --white: #ffffff;
    --pill: #dfe8f4;
    --pill-ink: #1b2a4a;
  }
  * { box-sizing: border-box; margin: 0; padding: 0; }
  html, body { width: 1043px; height: 1200px; overflow: hidden; background: var(--page); }
  .sheet { position: relative; width: 1043px; height: 1200px; }

  .option-label {
    position: absolute; left: 9px;
    font: 42px "Arimo", Arial, sans-serif; color: var(--label); letter-spacing: 1px;
  }

  .card {
    position: absolute; left: 412px; width: 600px; height: 356px; overflow: hidden;
    box-shadow: 3px 4px 10px rgba(0,0,0,0.45);
    font-family: "PT Sans", Tahoma, sans-serif; color: var(--ink);
  }
  .card > * { position: absolute; }

  .brand { left: 22px; top: 30px; display: flex; align-items: center; gap: 12px; }
  .brand-dot { width: 26px; height: 26px; border-radius: 50%; background: var(--brand); }
  .brand-name { font-weight: 700; font-size: 34px; color: var(--brand); white-space: nowrap; }

  .location-band {
    left: 0; right: 0; bottom: 0; background: var(--band);
    border-top: 3px solid var(--band-line);
    display: flex; justify-content: center; align-items: center; gap: 26px;
    color: var(--white); font-size: 25px;
  }

  .pickup-pill {
    left: 50%; transform: translateX(-50%);
    background: var(--pill); border-radius: 16px; padding: 2px 18px;
    font: 700 19px "Dancing Script", cursive; color: var(--pill-ink); white-space: nowrap;
  }

  /* Option 1 – water */
  .card-water { top: 26px; background: linear-gradient(180deg, var(--water-light) 0%, var(--water-mid) 55%, var(--water-deep) 100%); }
  .card-water .person { left: 14px; top: 220px; }
  .card-water .person-name { font-size: 22px; font-weight: 700; }
  .card-water .person-line { font-size: 16px; line-height: 21px; }
  .card-water .address { right: 14px; top: 222px; text-align: right; font-size: 17px; line-height: 21px; }
  .card-water .location-band { height: 48px; background: rgba(27,99,179,0.55); }

  /* Option 2 – white to blue */
  .card-fade { top: 429px; background: linear-gradient(180deg, #ffffff 0%, #eef3fa 30%, #9dbde6 65%, #3f7cc8 100%); }
  .card-fade .person { left: 14px; top: 120px; }
  .card-fade .person-name { font-size: 23px; font-weight: 700; letter-spacing: 0.5px; }
  .card-fade .person-line { font-size: 17px; line-height: 22px; }
  .card-fade .address { right: 16px; top: 123px; text-align: right; font-size: 17px; line-height: 22px; }
  .card-fade .services { left: 0; right: 0; top: 212px; text-align: center; font-size: 17px; line-height: 24px; }
  .card-fade .pickup-pill { top: 270px; }
  .card-fade .location-band { height: 52px; }

  /* Option 3 – solid blue */
  .card-solid { top: 825px; background: var(--card3); color: var(--white); font-family: "Tinos", "Times New Roman", serif; }
  .card-solid .brand-dot { background: var(--white); }
  .card-solid .brand-name { color: var(--white); font-family: "PT Sans", Tahoma, sans-serif; }
  .card-solid .details { left: 0; right: 0; top: 148px; text-align: center; }
  .card-solid .person-name { font-size: 23px; font-weight: 700; letter-spacing: 0.5px; }
  .card-solid .person-line { font-size: 18px; line-height: 23px; margin-top: 8px; }
  .card-solid .contact-italic { font-style: italic; font-size: 18px; line-height: 22px; margin-top: 6px; }
  .card-solid .pickup-pill { top: 265px; }
  .card-solid .location-band { height: 56px; background: var(--card3); font-family: "Tinos", serif; font-style: italic; font-weight: 700; font-size: 27px; }
</style>
</head>
<body>
<main class="sheet">

  <div class="option-label" style="top:180px">BC DESIGN 1</div>
  <div class="option-label" style="top:580px">BC DESIGN 2</div>
  <div class="option-label" style="top:978px">BC DESIGN 3</div>

  <section class="card card-water">
    <div class="brand"><span class="brand-dot"></span><span class="brand-name">Quill Press Wash</span></div>
    <div class="person">
      <div class="person-name">Morgan Ellery</div>
      <div class="person-line">M: 0412 587 630</div>
      <div class="person-line">E: morgan@quillpresswash.com.au</div>
    </div>
    <div class="address">18 Harbourview Rd<br>Seabrook Qld 4190<br>P: (07) 3521 8846</div>
    <div class="location-band"><span>Seabrook</span><span>|</span><span>Ashmere</span><span>|</span><span>Kelsey Pt</span></div>
  </section>

  <section class="card card-fade">
    <div class="brand"><span class="brand-dot"></span><span class="brand-name">Quill Press Wash</span></div>
    <div class="person">
      <div class="person-name">MORGAN ELLERY</div>
      <div class="person-line">Cell: 0412 587 630</div>
      <div class="person-line">Tel: (07) 3521 8846</div>
    </div>
    <div class="address">morgan@quillpresswash.com.au<br>18 Harbourview Rd<br>Seabrook Qld 4190</div>
    <div class="services">Dry Cleaning &bull; Repairs and Alterations &bull; Laundered Shirts<br>Wedding Gowns &bull; Household Items &bull; Curtain Cleaning</div>
    <div class="pickup-pill">Pick Up And Delivery – Your Home Or Workplace</div>
    <div class="location-band"><span>Seabrook</span><span>|</span><span>Ashmere</span><span>|</span><span>Kelsey Pt</span></div>
  </section>

  <section class="card card-solid">
    <div class="brand"><span class="brand-dot"></span><span class="brand-name">Quill Press Wash</span></div>
    <div class="details">
      <div class="person-name">MORGAN ELLERY</div>
      <div class="person-line">Cell: 0412 587 630 &bull; Tel: (07) 3521 8846</div>
      <div class="contact-italic">morgan@quillpresswash.com.au<br>18 Harbourview Rd., Seabrook Qld 4190</div>
    </div>
    <div class="pickup-pill">Pick Up And Delivery – Your Home Or Workplace</div>
    <div class="location-band"><span>Seabrook</span><span>|</span><span>Ashmere</span><span>|</span><span>Kelsey Pt</span></div>
  </section>

</main>
</body>
</html>
```